Non-profit organization requires InDesign based template for a educational booklet

***Overview***
Our business "The Coastal Brightpath Centre for Skills and Learning" is a not for profit organisation working in vocational education both in the Australian and international markets. While we work within many professional contexts, we also work with projects in developing countries assisting to build institutional capacity in the education industry, upskilling in disadvantaged communities to ultimately facilitate positive development outcomes.

Our project is looking to deliver agricultural-based education units that will be delivered in booklet form. Vocational students will use these unit booklets for self-paced or classroom group study. The front of each unit will have a nice graphical cover page, contents and details about learning in the unit. This will be followed by about 15 pages of educational content with plenty of pictures and other material such as tables and graphs to illustrate learning points. This will then be followed by a short question sheet with space for students to write answers, followed by Activity sheets where students put into practice skills from the unit.

***The designed template should have***
* Cover page;
* Content page;
* Two (2) different introduction pages (two for variation);
* Three (3) different pages for lesson text – these pages will be the main study pages for the students, 3 for variation;
* Activity page - like an activity worksheet;
* Question page - page with questions or reflections that the students need to answer - a space under each question for students to write;

***Design preferences***

*Font – an inDesign default font please like Calibri – text built on a base Normal font 11pt, then headings H1, H2 etc... from that basis e.g. 24pt for H1 etc... the size up to the designer.

Happy to see creativity of graphic artists with the above themes.

Target Market(s)

In the requested project, I require an Adobe InDesign template (file in .indd) to be designed that will have particular characteristics suited to students who are:

* Age 15-17;
* Have the educational equivalent to Australian and US education standard of Yr 8;
* Attending vocational school - vocational schools are between secondary high school and University and are usually used to produce graduates within the skill trade area;
* Agricultural theme in the template;
* Sustainability theme (agricultural sustainability) as well;

Students are from very poor rural farming families in growing rice, coconut, rambutan, mangoes, cocoa, palm oil... - very SE Asian agricultural landscape.

Students are used to black and white government textbooks which are very dry, largely dull in design and colour – we do not want this!

Industry/Entity Type

Agriculture

Font styles to use
Sans Serif

Colors

Designer to choose colors to be used in the design.

Requirements
Must have
• * Final file must be in an editable Adobe Indesign file (.indd), with editable layers;
• * SE Asian agricultural theme in the template;
• * design must not look like dull and boring textbooks or corporate training booklets; * design should be vibrant and interesting but also not distracting from the lesson (i.e. it is not too garish);
• * suitable colours (it will be printed full colour) easy on the eye for students of the age group - colours related to agriculture;
• *Modern look and feel;
Should not have
• * design must not look like dull and boring textbooks or corporate training booklets;

```html
<!DOCTYPE html>
<html lang="en">
<head>
<meta charset="utf-8">
<title>Coastal Brightpath – Unit Cover</title>
<link rel="stylesheet" href="https://fonts.googleapis.com/css2?family=Aldrich&display=swap">
<style>
  :root {
    --page-bg: #e6e6e6;
    --forest: #0b6a55;
    --forest-deep: #085a48;
    --cream: #f6eec8;
    --sky: #1fb0dc;
    --sun: #f8c21d;
    --amber: #f29a1f;
    --title: #ffffff;
  }
  * { margin: 0; padding: 0; box-sizing: border-box; }
  html, body { width: 1200px; height: 1200px; overflow: hidden; background: var(--page-bg); }
  .canvas { width: 1200px; height: 1200px; display: flex; align-items: center; justify-content: center; }
  .cover { position: relative; width: 790px; height: 1118px; overflow: hidden; background: var(--forest); }
  .cover-art { position: absolute; inset: 0; width: 100%; height: 100%; display: block; }
  .cover-title {
    position: absolute; left: 90px; top: 132px;
    font-family: "Aldrich", sans-serif; font-size: 34px; line-height: 39px;
    color: var(--title); text-transform: uppercase; font-weight: 400; letter-spacing: 0;
  }
  .title-dot {
    position: absolute; left: 74px; top: 318px; width: 6px; height: 6px;
    border: 1.5px solid var(--sky); border-radius: 50%;
  }
</style>
</head>
<body>
<div class="canvas">
  <section class="cover">
    <svg class="cover-art" viewBox="0 0 790 1118" preserveAspectRatio="none" xmlns="http://www.w3.org/2000/svg">
      <defs>
        <linearGradient id="mapTone" x1="0" y1="0" x2="0" y2="1">
          <stop offset="0" stop-color="#075443"/>
          <stop offset="1" stop-color="#0b6a55" stop-opacity="0"/>
        </linearGradient>
        <linearGradient id="arcBand" x1="0" y1="0" x2="1" y2="0">
          <stop offset="0" stop-color="#1fb0dc"/>
          <stop offset="0.35" stop-color="#6cbf9a"/>
          <stop offset="0.7" stop-color="#b9b84a"/>
          <stop offset="1" stop-color="#e2b42a"/>
        </linearGradient>
        <linearGradient id="foliage" x1="0" y1="0" x2="1" y2="1">
          <stop offset="0" stop-color="#7fd0c6"/>
          <stop offset="0.25" stop-color="#e9e38e"/>
          <stop offset="0.45" stop-color="#f6c24a"/>
          <stop offset="0.62" stop-color="#f39a22"/>
          <stop offset="0.8" stop-color="#f6b64a"/>
          <stop offset="1" stop-color="#4fc3e2"/>
        </linearGradient>
        <linearGradient id="groundBand" x1="0" y1="0" x2="1" y2="1">
          <stop offset="0" stop-color="#f9d46a"/>
          <stop offset="0.5" stop-color="#f6bf3c"/>
          <stop offset="1" stop-color="#f1a92a"/>
        </linearGradient>
        <linearGradient id="rightPanel" x1="0" y1="0" x2="0" y2="1">
          <stop offset="0" stop-color="#0b6a55"/>
          <stop offset="0.4" stop-color="#0d7f76"/>
          <stop offset="0.55" stop-color="#1fb0dc"/>
          <stop offset="0.72" stop-color="#f8c81d"/>
          <stop offset="1" stop-color="#dba04e"/>
        </linearGradient>
        <linearGradient id="stalkPhotos" x1="0" y1="0" x2="0" y2="1">
          <stop offset="0" stop-color="#c9a24f"/>
          <stop offset="0.18" stop-color="#7aa64a"/>
          <stop offset="0.35" stop-color="#3f8a2e"/>
          <stop offset="0.52" stop-color="#c99a4a"/>
          <stop offset="0.7" stop-color="#5f8a35"/>
          <stop offset="0.85" stop-color="#b08a4a"/>
          <stop offset="1" stop-color="#9a6a35"/>
        </linearGradient>
      </defs>

      <rect class="field-forest" width="790" height="1118" fill="var(--forest)"/>
      <rect class="map-area" role="img" aria-label="Faint map of Southeast Asia across the top of the cover"
            x="0" y="0" width="790" height="360" fill="url(#mapTone)"/>

      <ellipse class="arc-band" cx="560" cy="1300" rx="1500" ry="885" fill="url(#arcBand)"/>
      <ellipse class="foliage-art" role="img" aria-label="Stylised tropical palm and monstera leaf pattern"
               cx="560" cy="1320" rx="1460" ry="830" fill="url(#foliage)"/>
      <path class="ground-band" d="M0,805 Q320,795 617,990 L617,1118 L0,1118 Z" fill="url(#groundBand)"/>

      <rect class="right-panel" x="617" y="280" width="173" height="838" fill="url(#rightPanel)"/>

      <rect class="stalk-gallery" role="img" aria-label="Wheat-stalk ornament framing twelve farm photographs: wheat fields, ploughed land, grazing cattle, crop rows, a harvester, vineyards and an orchard lane"
            x="482" y="68" width="268" height="830" rx="6" fill="url(#stalkPhotos)" opacity="0.92"/>

      <line class="stem" x1="617" y1="0" x2="617" y2="1118" stroke="var(--cream)" stroke-width="4"/>
    </svg>

    <span class="title-dot"></span>
    <h1 class="cover-title">The<br>Coastal<br>Brightpath<br>Centre for Skills<br>and Learning</h1>
  </section>
</div>
</body>
</html>
```